Postcard design to acquire new clients for my Property Management Company

I'm looking for a postcard design that I can send to prospective clients detailing information about my company and services.
Postcard should be eye catching and contain information from www.brightkeeplm.com. I've provided a few screen shots for the most important information and my logo.
Target Market(s)
Real Estate
Industry/Entity Type
Real Estate
Font styles to use
Sans Serif
Requirements
Must have
- Must be eye catching!! this will be a direct mail piece - I'd like for the card to be read and not tossed in the trash immediately.
Design que from the logo.
A place to write / print the receipts name and address.
our physical address - 2287 Marden Lane, Lubbock, TX 79382.
Should not have
- the contact information on the business card is not accurate - please use info from website.

```html
<!DOCTYPE html>
<html lang="en">
<head>
<meta charset="utf-8">
<title>Brightkeep Lease Management – Postcard</title>
<link href="https://fonts.googleapis.com/css2?family=Montserrat:ital,wght@0,400;0,500;0,600;0,700;0,800;1,500;1,800&display=swap" rel="stylesheet">
<style>
  :root{
    --navy:#2c4d7d;
    --hero-blue:#3e5d8c;
    --slate:#a4a4a4;
    --panel:#e1e1e3;
    --panel-edge:#b9b9bb;
    --ink:#1e1e1e;
    --muted:#8a8a8a;
    --page:#dcdde0;
    --white:#ffffff;
  }
  *{box-sizing:border-box;margin:0;padding:0}
  html,body{width:884px;height:1200px;overflow:hidden;background:var(--page);font-family:'Montserrat',sans-serif;color:var(--ink)}
  .canvas{position:relative;width:884px;height:1200px}
  .card{position:absolute;left:70px;width:741px;background:var(--white);box-shadow:0 6px 18px rgba(0,0,0,.18);overflow:hidden}
  .card-front{top:56px;height:494px}
  .card-back{top:636px;height:493px}
  .abs{position:absolute}

  /* front */
  .brand{left:23px;top:26px;color:var(--navy);font-weight:700;line-height:1}
  .brand-name{font-size:23px;letter-spacing:5px;display:block}
  .brand-sub{font-size:10px;letter-spacing:2.6px;display:block;margin-top:4px}
  .contact-line{right:23px;top:50px;font-size:11.5px;display:flex;align-items:center;gap:5px;color:var(--ink)}
  .contact-line svg{width:11px;height:11px}
  .contact-line .sep{width:10px}
  .hero{left:23px;top:75px;width:694px;height:193px}
  .hero-title{left:476px;top:94px;color:var(--white);font-weight:800;font-size:25px;line-height:26.5px}
  .hero-sub{left:476px;top:218px;color:var(--white);font-weight:600;font-size:12.5px;line-height:14.5px}

  .feature{left:23px;height:60px}
  .feature svg.band{position:absolute;left:0;top:0}
  .feature-icon{position:absolute;left:9px;top:50%;transform:translateY(-50%);width:31px;height:31px}
  .feature-text{position:absolute;left:58px;top:50%;transform:translateY(-50%);color:var(--white);font-weight:700;font-size:12px;line-height:12.5px}

  .plan{top:285px;width:160px;margin-left:-80px;text-align:center}
  .plan-title{color:var(--navy);font-weight:800;font-size:13.5px;line-height:16px}
  .plan-tag{color:var(--muted);font-weight:500;font-size:9.5px;margin-top:3px}
  .plan-rate{display:inline-block;margin-top:6px;width:65px;height:27px;background:#d4d4d4;color:var(--navy);font-weight:800;font-size:20px;line-height:27px}
  .plan-body{margin-top:7px;font-size:8.6px;line-height:17.1px}
  .divider{top:287px;width:1px;height:183px;background:var(--slate)}

  /* back */
  .services-title{left:36px;top:23px;color:var(--white);font-weight:800;font-style:italic;font-size:21px;line-height:28px}
  .services-tag{left:286px;top:23px;color:#555;font-style:italic;font-weight:500;font-size:11.5px;line-height:13px}
  .service{width:110px;margin-left:-55px;text-align:center}
  .service svg{width:22px;height:22px;display:block;margin:0 auto}
  .service h3{color:var(--navy);font-weight:700;font-size:10px;margin-top:3px;line-height:12px}
  .service p{font-size:8.3px;line-height:11.5px;margin-top:2px}
  .svc-rule{width:1px;background:#9a9a9a}
  .stamp{left:637px;top:41px;width:61px;height:61px;border:1px solid #9a9a9a}
  .addr-line{height:1px;background:#aaa}
  .cta{left:102px;top:436px;color:var(--white);font-size:11.5px;line-height:15.5px}
  .cta strong{font-weight:700;font-size:12px;letter-spacing:.3px}
  .contact-badge{left:37px;top:430px;width:50px;height:54px;background:var(--slate);border-radius:0 0 6px 6px;color:var(--white);text-align:center;font-size:7px;font-weight:600;line-height:8px;padding-top:6px}
  .contact-badge svg{width:30px;height:22px;display:block;margin:0 auto 1px}
</style>
</head>
<body>
<div class="canvas">

  <!-- FRONT -->
  <section class="card card-front">
    <div class="abs brand">
      <span class="brand-name">BRIGHTKEEP</span>
      <span class="brand-sub">LEASE MANAGEMENT</span>
    </div>
    <div class="abs contact-line">
      <span>2287 Marden Lane, Lubbock, TX 79382</span>
      <svg viewBox="0 0 12 12"><path d="M6 0.5a4 4 0 0 0-4 4c0 3 4 7 4 7s4-4 4-7a4 4 0 0 0-4-4zm0 5.5a1.5 1.5 0 1 1 0-3 1.5 1.5 0 0 1 0 3z" fill="#9a9a9a"/></svg>
      <span class="sep"></span>
      <span>www.brightkeeplm.com</span>
      <svg viewBox="0 0 12 12" fill="none" stroke="#9a9a9a" stroke-width="0.9"><circle cx="6" cy="6" r="5"/><ellipse cx="6" cy="6" rx="2.2" ry="5"/><path d="M1 6h10M2 3.3h8M2 8.7h8"/></svg>
    </div>

    <svg class="abs hero" viewBox="0 0 694 193">
      <defs>
        <linearGradient id="photoTone" x1="0" y1="0" x2="1" y2="1">
          <stop offset="0" stop-color="#c9c9c9"/>
          <stop offset="0.55" stop-color="#8d8d8d"/>
          <stop offset="1" stop-color="#5a5a5a"/>
        </linearGradient>
      </defs>
      <polygon points="0,0 424,0 347,193 0,193" fill="url(#photoTone)" role="img" aria-label="Photo: business team of three colleagues meeting at a desk"/>
      <polygon points="424,0 694,0 694,193 347,193" fill="var(--hero-blue)"/>
    </svg>
    <h1 class="abs hero-title">Choose The<br>Right Property<br>Management<br>System</h1>
    <p class="abs hero-sub">We provide unbeatable support<br>for your rental home.</p>

    <div class="abs feature" style="top:287px;width:212px;height:62px">
      <svg class="band" width="212" height="62"><rect width="49" height="62" fill="var(--navy)"/><polygon points="49,0 212,0 188,62 49,62" fill="var(--slate)"/></svg>
      <svg class="feature-icon" viewBox="0 0 32 32" fill="none" stroke="#fff" stroke-width="1.6"><path d="M20 4H7v24h10"/><path d="M11 10h8M11 14h8M11 18h5"/><circle cx="23" cy="23" r="5"/><path d="M20.8 23l1.6 1.6 3-3M27 27l3 3"/></svg>
      <div class="feature-text">Put Our Local<br>Experience<br>to the Test</div>
    </div>
    <div class="abs feature" style="top:354px;width:186px;height:53px">
      <svg class="band" width="186" height="53"><rect width="49" height="53" fill="var(--navy)"/><polygon points="49,0 186,0 165,53 49,53" fill="var(--slate)"/></svg>
      <svg class="feature-icon" viewBox="0 0 32 32" fill="none" stroke="#fff" stroke-width="1.6"><path d="M7 17a9 9 0 0 1 18 0v4"/><rect x="5" y="16" width="4" height="7" rx="1.5"/><rect x="23" y="16" width="4" height="7" rx="1.5"/><path d="M25 23c0 3-3 5-7 5h-2"/></svg>
      <div class="feature-text">We Offer<br>Unbeatable<br>Support</div>
    </div>
    <div class="abs feature" style="top:412px;width:163px;height:60px">
      <svg class="band" width="163" height="60"><rect width="49" height="60" fill="var(--navy)"/><polygon points="49,0 163,0 139,60 49,60" fill="var(--slate)"/></svg>
      <svg class="feature-icon" viewBox="0 0 32 32" fill="none" stroke="#fff" stroke-width="1.6"><path d="M26 11A12 12 0 1 0 28 18" /><path d="M22 8l4 3 1-5" /><text x="9" y="20" fill="#fff" stroke="none" font-family="Montserrat, sans-serif" font-size="10" font-weight="700">24</text></svg>
      <div class="feature-text">24/7<br>Online Portal<br>Access</div>
    </div>

    <div class="abs plan" style="left:306px">
      <div class="plan-title">Lease Only</div>
      <div class="plan-tag">- You Just Need Tenants -</div>
      <div class="plan-rate">9%</div>
      <div class="plan-body">of annual lease Professional<br>Photography Marketing &amp;<br>Advertising Property Showings<br>Tenant Screening &amp;<br>Qualifications Lease Execution<br>Move In Coordination</div>
    </div>
    <div class="abs divider" style="left:385px"></div>
    <div class="abs plan" style="left:476px">
      <div class="plan-title">Full Service</div>
      <div class="plan-tag">- Our Most Popular -</div>
      <div class="plan-rate">10%</div>
      <div class="plan-body">of monthly rent Includes Leasing<br>Service 24/7 Emergency Response<br>Move In &amp; Out Inspections Professional<br>Lease Enforcement Schedule &amp;<br>Oversee all Repairs Pay all Invoices<br>Monthly &amp; Year End Statements<br>Annual Market Rent Analysis</div>
    </div>
    <div class="abs divider" style="left:568px"></div>
    <div class="abs plan" style="left:645px">
      <div class="plan-title">Premium Service</div>
      <div class="plan-tag">- Our Premier Service -</div>
      <div class="plan-rate">12%</div>
      <div class="plan-body">of monthly rent Includes Full<br>Service Features Professional<br>Video Marketing Home<br>Warranty Coordination Tenant<br>Retention Program</div>
    </div>
  </section>

  <!-- BACK -->
  <section class="card card-back">
    <svg class="abs" width="741" height="493" style="left:0;top:0">
      <polygon points="0,0 519,0 347,431 0,431" fill="var(--panel)"/>
      <polygon points="511,0 519,0 355,431 347,431" fill="var(--panel-edge)"/>
      <polygon points="0,21 285,21 271,49 0,49" fill="var(--navy)"/>
      <polygon points="0,431 356,431 340,476 0,476" fill="var(--navy)"/>
    </svg>
    <h2 class="abs services-title">Discover Our Services</h2>
    <p class="abs services-tag">&nbsp;We Offer Full-service Property<br>Management Solutions</p>

    <div class="abs svc-rule" style="left:147px;top:88px;height:79px"></div>
    <div class="abs svc-rule" style="left:271px;top:88px;height:79px"></div>
    <div class="abs svc-rule" style="left:147px;top:203px;height:79px"></div>
    <div class="abs svc-rule" style="left:271px;top:203px;height:79px"></div>
    <div class="abs svc-rule" style="left:147px;top:321px;height:91px"></div>

    <div class="abs service" style="left:86px;top:59px">
      <svg viewBox="0 0 24 24" fill="var(--navy)"><path d="M12 3 1.5 11.5l1.3 1.5L4.5 11.7V21h5.5v-6h4v6h5.5v-9.3l1.7 1.3 1.3-1.5L17 7.4V4h-2.5v1.4z"/></svg>
      <h3>Property Marketing</h3>
      <p>Tired of waiting for weeks on end, hoping to find a new tenant? Let us take over your marketing for you and we'll find a qualified renter quickly.</p>
    </div>
    <div class="abs service" style="left:208px;top:59px">
      <svg viewBox="0 0 24 24" fill="var(--navy)"><circle cx="8" cy="7" r="4"/><circle cx="17" cy="8" r="3.3"/><path d="M0 21c0-5 3.5-8 8-8s8 3 8 8z"/><path d="M16.5 13c4 0 7.5 2.5 7.5 7h-6.5c0-3-0.6-5-1-7z"/></svg>
      <h3>Tenant Screening</h3>
      <p>We don't just find someone to rent your home—we find the best renters. We screen all applications using fair housing guidelines to protect you.</p>
    </div>
    <div class="abs service" style="left:333px;top:59px">
      <svg viewBox="0 0 24 24" fill="none" stroke="var(--navy)" stroke-width="2.4"><path d="M12 1v22"/><path d="M17 6.5c-1-1.5-2.7-2-5-2-2.8 0-4.5 1.3-4.5 3.3 0 4.7 9.5 2.7 9.5 7.8 0 2-1.9 3.5-5 3.5-2.3 0-4.2-.7-5.2-2.4"/></svg>
      <h3>Rent Collection</h3>
      <p>Stop guessing when you'll receive your rental earnings every month and say hello to consistent payments. We keep your tenants current.</p>
    </div>

    <div class="abs service" style="left:86px;top:174px">
      <svg viewBox="0 0 24 24" fill="var(--navy)"><path d="M9 2h6l6 4-3 3-3-2-9.5 14.5-3-2L12 6 9 4z"/></svg>
      <h3>Maintenance</h3>
      <p>Still scrambling to respond to repair requests every time you receive a tenant call? Let us coordinate repair work on your behalf!</p>
    </div>
    <div class="abs service" style="left:208px;top:174px">
      <svg viewBox="0 0 24 24" fill="none" stroke="var(--navy)" stroke-width="2.6"><circle cx="10" cy="10" r="6.5"/><path d="M15 15l7 7"/></svg>
      <h3>Property Inspections</h3>
      <p>Inspections form an important part of our proactive property management approach. We visit every home in our portfolio regularly.</p>
    </div>
    <div class="abs service" style="left:333px;top:174px">
      <svg viewBox="0 0 24 24" fill="none" stroke="var(--navy)" stroke-width="2"><path d="M2 2v20h22"/><path d="M7 18v-6M11 18V8M15 18v-8M19 18V5"/></svg>
      <h3>Financial Reporting</h3>
      <p>Keep a handle on your real estate performance. We generate monthly statements so you can review income &amp; expenses at a moment's notice.</p>
    </div>

    <div class="abs service" style="left:86px;top:292px">
      <svg viewBox="0 0 24 24" fill="none" stroke="var(--navy)" stroke-width="2"><path d="M12 2 4 5v6c0 5.5 3.5 9.5 8 11 4.5-1.5 8-5.5 8-11V5z"/><path d="M12 3v18" /><path d="M12 3 19 5.7V11c0 4.8-3 8.5-7 10z" fill="var(--navy)"/></svg>
      <h3>Evictions</h3>
      <p>When things go wrong inside your rental home, rest easy with the experts on your side. We will handle evictions for you &amp; find new renters when its over.</p>
    </div>
    <div class="abs service" style="left:208px;top:292px">
      <svg viewBox="0 0 24 24" fill="none" stroke="var(--navy)" stroke-width="1.8"><path d="M12 3v18M7 21h10M3 6h18"/><path d="M5.5 6 2 14a3.5 3 0 0 0 7 0zM18.5 6 15 14a3.5 3 0 0 0 7 0z"/></svg>
      <h3>Legal Guidance</h3>
      <p>Don't accidentally violate one of the many ordinances and housing laws governing your relationship with your tenants. Let us keep you compliant.</p>
    </div>

    <div class="abs stamp"></div>
    <div class="abs addr-line" style="left:492px;top:231px;width:206px"></div>
    <div class="abs addr-line" style="left:476px;top:272px;width:222px"></div>
    <div class="abs addr-line" style="left:460px;top:314px;width:238px"></div>

    <div class="abs contact-badge">
      <svg viewBox="0 0 30 22" fill="#fff"><circle cx="15" cy="6" r="4.5"/><path d="M6 21c0-5 4-8 9-8s9 3 9 8z"/><circle cx="6" cy="9" r="3"/><circle cx="24" cy="9" r="3"/><path d="M0 20c0-3.5 2.5-6 6-6 1 0 2 .2 2.7.6C6.5 16 5.5 18 5.3 20zM30 20c0-3.5-2.5-6-6-6-1 0-2 .2-2.7.6 2.2 1.4 3.2 3.4 3.4 5.4z"/></svg>
      Contact<br>Our Team
    </div>
    <p class="abs cta">Give us a call now: <strong>(806) 555-0147</strong><br>Email us: <strong>info@brightkeeplm.com</strong></p>
  </section>

</div>
</body>
</html>
```